Webdesign für VORA Registrierung für die USA
Zielgruppe
Erstellung von Reisegenehmigungen (Visa)
Aufgabenstellung
- Orientierung an Vora.us
- es gibt kein Logo oder CD
- die Webseite soll seriös wirken

```html
<!DOCTYPE html>
<html lang="de">
<head>
<meta charset="utf-8">
<title>VORA – Travel Authorization</title>
<link rel="stylesheet" href="https://fonts.googleapis.com/css2?family=Open+Sans:wght@300;400;600;700;800&display=swap">
<style>
  :root {
    --navy-deep: #0f1f33;
    --navy-nav: #1d3550;
    --slate: #34536f;
    --heading-navy: #1f3a5a;
    --box-blue: rgba(58, 104, 150, 0.9);
    --red: #c4161c;
    --white: #ffffff;
    --stage: #e4e6e8;
    --sky-top: #5f8fbf;
    --sky-mid: #a9c3da;
    --water: #3d6d96;
  }
  * { box-sizing: border-box; margin: 0; padding: 0; }
  html, body { width: 1200px; height: 1200px; overflow: hidden; }
  body { background: var(--stage); font-family: "Open Sans", sans-serif; }

  .page-frame { position: absolute; left: 356px; top: 15px; width: 489px; height: 1170px; overflow: hidden; box-shadow: 0 4px 14px rgba(0,0,0,.25); }
  .page { position: absolute; left: 0; top: 0; width: 734px; height: 1757px; transform: scale(0.666); transform-origin: 0 0; background: var(--white); }

  .site-nav { position: absolute; left: 0; top: 0; width: 734px; height: 37px; background: var(--navy-nav); }
  .site-nav .home { position: absolute; left: 120px; top: 11px; }
  .site-nav ul { position: absolute; left: 152px; top: 14px; display: flex; gap: 10px; list-style: none; }
  .site-nav li { color: var(--white); font-size: 6px; font-weight: 700; letter-spacing: .3px; }
  .site-nav .domain { position: absolute; right: 120px; top: 10px; color: var(--white); font-size: 12px; font-weight: 700; }

  .hero { position: absolute; left: 0; top: 37px; width: 734px; height: 405px; }
  .hero .photo { position: absolute; inset: 0; background: linear-gradient(180deg, var(--sky-top) 0%, var(--sky-mid) 55%, #7d8f8f 82%, var(--water) 100%); }
  .hero .lang-select { position: absolute; left: 495px; top: 20px; width: 118px; height: 15px; background: var(--white); font-size: 5px; color: #555; padding: 4px 6px; }
  .hero .lang-select::after { content: ""; position: absolute; right: -12px; top: 3px; width: 6px; height: 6px; border-right: 1.5px solid var(--white); border-bottom: 1.5px solid var(--white); transform: rotate(45deg); }
  .hero .brand-word { position: absolute; left: 120px; top: 80px; font-size: 116px; font-weight: 800; color: #2d5b8d; opacity: .92; letter-spacing: -5px; line-height: 1; }
  .hero .title-frame { position: absolute; left: 295px; top: 131px; width: 317px; height: 146px; border: 2px solid var(--white); }
  .hero .title-text { position: absolute; right: 152px; top: 164px; text-align: right; line-height: 1.2; }
  .hero .title-text .accent { color: var(--red); font-size: 15px; font-weight: 700; letter-spacing: .6px; }
  .hero .title-text .plain { color: var(--heading-navy); font-size: 15px; font-weight: 300; letter-spacing: .6px; }
  .btn-apply { position: absolute; background: var(--red); color: var(--white); font-weight: 700; font-size: 13px; text-align: center; }
  .hero .btn-apply { left: 430px; top: 319px; width: 182px; height: 23px; line-height: 23px; }

  .how-it-works { position: absolute; left: 0; top: 442px; width: 734px; height: 225px; background: var(--slate); }
  .how-it-works h2 { position: absolute; left: 0; top: 32px; width: 734px; text-align: center; color: var(--white); font-size: 20px; font-weight: 700; letter-spacing: 1px; }
  .how-it-works .steps { position: absolute; left: 0; top: 0; }
  .step-label { position: absolute; width: 120px; text-align: center; color: var(--white); font-size: 10px; font-weight: 700; letter-spacing: 1.2px; line-height: 1.3; }

  .what-is { position: absolute; left: 0; top: 667px; width: 734px; height: 393px; }
  .what-is .photo { position: absolute; inset: 0; background: linear-gradient(180deg, #9fb2c0 0%, #c9b79a 40%, #9a7b5c 65%, #5f86a8 85%, #7ea8c8 100%); }
  .what-is .info-box { position: absolute; left: 121px; top: 40px; width: 239px; height: 146px; background: var(--box-blue); padding: 18px 19px; color: var(--white); }
  .what-is h2 { font-size: 19px; font-weight: 700; letter-spacing: .5px; margin-bottom: 10px; }
  .what-is p { font-size: 7.4px; line-height: 1.3; font-weight: 400; }

  .faq-row { position: absolute; left: 0; width: 734px; }
  .faq-row h2 { position: absolute; left: 121px; font-size: 20px; font-weight: 700; letter-spacing: .8px; line-height: 1.25; }
  .faq-row .answer { position: absolute; left: 370px; width: 243px; border: 3px solid; padding: 14px 18px; font-size: 7.4px; line-height: 1.3; }
  .who-needs { top: 1060px; height: 175px; background: var(--white); }
  .who-needs h2 { top: 36px; color: var(--heading-navy); }
  .who-needs .answer { top: 39px; height: 99px; border-color: var(--heading-navy); color: #4b5a6a; }
  .visa-waiver { top: 1235px; height: 177px; background: linear-gradient(90deg, #2a3f58 0%, #33506e 50%, #3b4f68 100%); }
  .visa-waiver h2 { top: 38px; color: var(--white); }
  .visa-waiver .answer { top: 39px; height: 99px; border-color: var(--white); color: var(--white); }

  .eligibility { position: absolute; left: 0; top: 1412px; width: 734px; height: 248px; background: var(--slate); }
  .eligibility h2 { position: absolute; left: 121px; top: 35px; color: var(--white); font-size: 20px; font-weight: 700; letter-spacing: .8px; line-height: 1.25; }
  .eligibility .intro { position: absolute; left: 121px; top: 128px; width: 205px; color: var(--white); font-size: 6.8px; line-height: 1.3; }
  .eligibility .answer { position: absolute; left: 370px; top: 40px; width: 243px; height: 85px; border: 3px solid var(--white); padding: 14px 18px; color: var(--white); font-size: 7.4px; line-height: 1.3; }
  .eligibility .citizenship { position: absolute; left: 370px; top: 145px; width: 226px; height: 15px; background: var(--white); color: #555; font-size: 6px; padding: 4px 9px; }
  .eligibility .citizenship-toggle { position: absolute; left: 596px; top: 145px; width: 15px; height: 15px; background: var(--slate); border: 1px solid var(--white); }
  .eligibility .citizenship-toggle::after { content: ""; position: absolute; left: 4px; top: 2px; width: 5px; height: 5px; border-right: 1.5px solid var(--white); border-bottom: 1.5px solid var(--white); transform: rotate(45deg); }
  .eligibility .btn-apply { left: 370px; top: 181px; width: 242px; height: 22px; line-height: 22px; }

  .site-footer { position: absolute; left: 0; top: 1660px; width: 734px; height: 97px; background: var(--navy-deep); text-align: center; color: var(--white); }
  .site-footer .domain { position: absolute; left: 0; top: 18px; width: 734px; font-size: 13px; font-weight: 600; letter-spacing: 3px; }
  .site-footer .links { position: absolute; left: 0; top: 47px; width: 734px; font-size: 5.5px; font-weight: 700; letter-spacing: .3px; }
  .site-footer .copyright { position: absolute; left: 0; top: 71px; width: 734px; font-size: 5px; opacity: .7; }
</style>
</head>
<body>
<div class="page-frame">
  <div class="page">

    <nav class="site-nav">
      <svg class="home" width="12" height="11" viewBox="0 0 12 11"><path d="M6 0 L12 5 H10 V11 H7 V7 H5 V11 H2 V5 H0 Z" fill="#6f9cc8"/></svg>
      <ul>
        <li>VORA APPLICATION</li>
        <li>VERIFY - LOCATE - CHECK VORA STATUS</li>
        <li>VORA NUMBER</li>
        <li>HELP</li>
      </ul>
      <span class="domain">VORA.DE</span>
    </nav>

    <header class="hero">
      <div class="photo" role="img" aria-label="Photo of a harbour monument in front of a city skyline under a blue sky"></div>
      <div class="lang-select">Select Language:</div>
      <div class="brand-word">VORA</div>
      <div class="title-frame"></div>
      <div class="title-text">
        <div class="accent">UNITED</div>
        <div class="accent">STATES TRAVEL</div>
        <div class="plain">AUTHORIZATION</div>
        <div class="plain">APPLICATION</div>
      </div>
      <div class="btn-apply">Click here to apply!</div>
    </header>

    <section class="how-it-works">
      <h2>HOW IT WORKS</h2>
      <svg class="steps" width="734" height="225" viewBox="0 0 734 225" fill="none" stroke="#ffffff" stroke-width="1.2">
        <line x1="210" y1="120" x2="275" y2="120"/>
        <line x1="330" y1="120" x2="397" y2="120"/>
        <line x1="452" y1="120" x2="521" y2="120"/>
        <circle cx="182" cy="120" r="27"/>
        <path d="M170 132 L172 124 L190 106 L196 112 L178 130 Z M186 110 L192 116"/>
        <circle cx="302" cy="120" r="27"/>
        <path d="M284 126 L296 120 L294 104 L298 104 L306 117 L318 111 Q324 110 321 115 L310 122 L314 136 L310 136 L303 126 L291 132 Z"/>
        <circle cx="425" cy="120" r="27"/>
        <rect x="413" y="104" width="24" height="32" rx="2"/>
        <circle cx="425" cy="118" r="7"/>
        <line x1="418" y1="118" x2="432" y2="118"/>
        <line x1="418" y1="129" x2="432" y2="129"/>
        <circle cx="549" cy="120" r="27"/>
        <path d="M545 144 V110 L549 98 L553 110 V144 M553 112 L558 96"/>
      </svg>
      <div class="step-label" style="left:122px;top:167px">APPLY<br>ONLINE</div>
      <div class="step-label" style="left:242px;top:167px">TRAVEL TO<br>THE U.S.</div>
      <div class="step-label" style="left:370px;top:167px">IMMIGRATION</div>
      <div class="step-label" style="left:489px;top:167px">WELCOME<br>TO THE U.S.</div>
    </section>

    <section class="what-is">
      <div class="photo" role="img" aria-label="Photo of two people in a rooftop pool overlooking a city skyline at sunset"></div>
      <div class="info-box">
        <h2>WHAT IS VORA?</h2>
        <p>VORA stands for Visitor Online Registration Access. VORA is an online application system developed by the United States government to pre-screen travelers before they are allowed to board an airplane or ship bound for the United States. Starting on January 12, 2009, any person entering the United States under the visa waiver program is required to hold an approved VORA Travel Authorization.</p>
      </div>
    </section>

    <section class="faq-row who-needs">
      <h2>WHO NEEDS<br>TO APPLY FOR<br>VORA?</h2>
      <p class="answer">All travelers entering the United States (by air or sea) under the visa waiver program are required to hold a valid VORA travel authorization. The purpose of VORA is to allow the Border Travel Service to pre-screen all Visa Waiver Travelers before they leave their respective countries. U.S.-bound travelers are recommended to apply for a Travel Authorization at least 72 hours prior to departure.</p>
    </section>

    <section class="faq-row visa-waiver" role="img" aria-label="Dark blue photo background with a government building and flags">
      <h2>WHAT IS THE<br>VISA WAIVER<br>PROGRAM?</h2>
      <p class="answer">The visa waiver program is a U.S. government program that enables citizens and nationals from the Visa Waiver Countries to enter the United States for tourism or business purposes for up to 90 days without obtaining a visa. The advantage of entering the United States under the visa waiver program is that you can travel to the United States on short notice without obtaining a visa.</p>
    </section>

    <section class="eligibility">
      <h2>FREE VORA<br>ELIGIBILITY<br>TEST</h2>
      <p class="intro">The VORA application system is entirely online. There are no forms that need to be printed and you do not have to go to a U.S. Embassy or Consulate in person. Download the VORA Application Guide and apply today!</p>
      <p class="answer">Only citizens of Visa Waiver Countries are allowed to apply for VORA. It is important to know if you qualify for VORA before you submit your application. Use the drop-down menu on the left to select your nationality and click on „Submit".</p>
      <div class="citizenship">Select Your Citizenship:</div>
      <div class="citizenship-toggle"></div>
      <div class="btn-apply">Click here to apply!</div>
    </section>

    <footer class="site-footer">
      <div class="domain">VORA.DE</div>
      <div class="links">HOME &nbsp;|&nbsp; APPLICATION &nbsp;|&nbsp; FAQ &nbsp;|&nbsp; PRIVACY POLICY &nbsp;|&nbsp; TERMS and CONDITIONS &nbsp;|&nbsp; CONTACT US</div>
      <div class="copyright">© 2017 vora.de</div>
    </footer>

  </div>
</div>
</body>
</html>
```